Business Card Design - Law Firm

We are a boutique law firm located near the beach in Manly, Australia. We have recently had a new logo designed and are revamping our business cards with the new logo.

We have recently had a business card design done for us but are not entirely happy with it. We are looking for something modern, simplistic but striking. We would like to see multiple designs.

We have attached a word document which includes our new logo and the current business card design which we are looking at moving away from.

We would like the business cards to be double sided. We would like the design to include something which we can print in gloss colour when we send it to the business card printers.

```html
<!DOCTYPE html>
<html lang="en">
<head>
<meta charset="utf-8">
<title>Harlow &amp; Partners Lawyers – Business Cards</title>
<link rel="stylesheet" href="https://fonts.googleapis.com/css2?family=Lato:wght@400;700&family=Montserrat:wght@600&display=swap">
<style>
  :root {
    --page-bg: #e6e4e0;
    --card-white: #ffffff;
    --card-dark: #111318;
    --brand-blue: #4a5ea8;
    --brand-gold: #b5a56e;
    --ink: #222222;
    --text-grey: #555555;
    --white: #ffffff;
  }
  * { box-sizing: border-box; margin: 0; padding: 0; }
  html, body { width: 1200px; height: 1023px; overflow: hidden; }
  body {
    background: var(--page-bg);
    position: relative;
    font-family: "Lato", sans-serif;
  }
  .card {
    position: absolute;
    left: 248px;
    width: 681px;
    height: 390px;
    box-shadow: -6px 6px 10px rgba(0,0,0,0.35);
  }
  .card--front { top: 87px; background: var(--card-white); }
  .card--back { top: 541px; background: var(--card-dark); }

  .firm-name {
    position: absolute;
    display: flex;
    align-items: center;
    gap: 10px;
    font-family: "Montserrat", sans-serif;
    font-weight: 600;
    letter-spacing: 1.5px;
    white-space: nowrap;
  }
  .firm-name__dot { border-radius: 50%; flex: none; }
  .card--front .firm-name {
    left: 0; width: 341px; top: 176px;
    justify-content: center;
    font-size: 17px; color: var(--ink);
  }
  .card--front .firm-name__dot { width: 14px; height: 14px; background: var(--brand-blue); }
  .card--back .firm-name {
    left: 0; width: 681px; top: 180px;
    justify-content: center;
    font-size: 26px; color: var(--white); letter-spacing: 3px;
  }
  .card--back .firm-name__dot { width: 20px; height: 20px; background: var(--brand-gold); }

  .divider {
    position: absolute;
    left: 341px; top: 104px;
    width: 1px; height: 182px;
    background: var(--brand-blue);
  }
  .contact {
    position: absolute;
    left: 370px; top: 96px;
    color: var(--text-grey);
  }
  .contact__name {
    font-weight: 700; font-size: 30px; line-height: 36px;
    color: var(--brand-blue); letter-spacing: -0.3px;
  }
  .contact__role { font-size: 16px; line-height: 20px; color: var(--ink); }
  .contact__address { margin-top: 10px; font-size: 16px; line-height: 24px; padding-left: 2px; }
  .contact__list { list-style: none; margin-top: 8px; font-size: 16px; }
  .contact__list li { display: flex; align-items: center; gap: 10px; height: 26px; }
  .contact__list svg { width: 15px; height: 15px; fill: var(--brand-blue); flex: none; }
</style>
</head>
<body>
  <section class="card card--front" aria-label="Business card front">
    <div class="firm-name"><span class="firm-name__dot"></span>Harlow &amp; Partners Lawyers</div>
    <div class="divider"></div>
    <div class="contact">
      <h1 class="contact__name">Mara Ellison</h1>
      <p class="contact__role">Practice Manager</p>
      <p class="contact__address">Suite 4, 12 Dune Street<br>BAYVIEW NSW 2100</p>
      <ul class="contact__list">
        <li><svg viewBox="0 0 16 16" aria-hidden="true"><path d="M1 5c0-2 3-3 7-3s7 1 7 3v1h-3V5H4v1H1zM3 7h10l1 7H2zm5 2a2 2 0 100 4 2 2 0 000-4z"/></svg>(02) 9000 4187</li>
        <li><svg viewBox="0 0 16 16" aria-hidden="true"><path d="M1 3h14v10H1zm1.5 1.5v.3L8 9l5.5-4.2v-.3zm0 2v5h2.5zm11 0L11 11.5h2.5zM6 8.5l-3 3.5h10l-3-3.5-2 1.5z"/></svg>mara.ellison@harlowlaw.com.au</li>
        <li><svg viewBox="0 0 16 16" aria-hidden="true"><path d="M8 1a7 7 0 110 14A7 7 0 018 1zm0 1.3a5.7 5.7 0 100 11.4A5.7 5.7 0 008 2.3zM7.4 3v4.4H3.4v1.2h4v4.4h1.2V8.6h4V7.4h-4V3z"/></svg>www.harlowpartners.com.au</li>
      </ul>
    </div>
  </section>

  <section class="card card--back" aria-label="Business card back">
    <div class="firm-name"><span class="firm-name__dot"></span>Harlow &amp; Partners Lawyers</div>
  </section>
</body>
</html>
```